Group training gym/bootcamp needs a web design

We need a website for our gym that is based in Sydney. We have indoor functional training classes and outdoor bootcamp classes. We would like the web site to have a video (to be created) and photo gallery. I would like the site made on word press and i would like to be able to make minor changes such as changing images and text without having to use a designer.

The website should have the following pages: home page; the gym; the bootcamp; photo gallery; about us; contact.

I have uploaded our logo and i would like to keep to these colour (blue,yellow,silver) and black is also allowed

Target Market(s)

18-50 male and female

Industry/Entity Type

Gym

Coding

Coded - Design and coding required

Number of Pages Required

5+ page

Font styles to use
Sans Serif

Colors
0692cd
fbed22
1b1b1b
e8e8e8

Requirements
Must have
• The website should have the following pages: home page; the gym; the bootcamp; photo gallery; about us; contact.
• I have uploaded our logo and i would like to keep to these colour (blue,yellow,silver) and black is also allowed
• Video upload and photo upload

```html
<!DOCTYPE html>
<html lang="en">
<head>
<meta charset="utf-8">
<title>Corestride Fitness</title>
<link href="https://fonts.googleapis.com/css2?family=Open+Sans:wght@400;600;700&family=Oswald:wght@400;500&display=swap" rel="stylesheet">
<style>
:root{
  --blue:#1a76bd;
  --blue-dark:#1667a6;
  --yellow:#d9aa05;
  --yellow-btn:#e0b200;
  --silver:#b8bbbf;
  --black:#111111;
  --ink:#2b2b2b;
  --grey-text:#a6a6a6;
  --light:#ebebeb;
  --panel:#f4f4f4;
  --white:#ffffff;
}
*{margin:0;padding:0;box-sizing:border-box}
html,body{width:1200px;height:2564px;overflow:hidden}
body{position:relative;font-family:"Open Sans",Arial,sans-serif;color:var(--ink);background:var(--white)}
.abs{position:absolute}

/* top bar */
.topbar{left:0;top:0;width:1200px;height:44px;background:var(--black)}
.topbar .phone{left:834px;top:12px;color:#e6e6e6;font-size:15px;font-weight:600;letter-spacing:.3px}
.btn-sm{top:7px;height:31px;border-radius:3px;font-size:13px;font-weight:600;display:flex;align-items:center;justify-content:center}
.btn-signin{left:967px;width:72px;background:var(--silver);color:#f4f4f4}
.btn-signup{left:1053px;width:73px;background:var(--yellow-btn);color:var(--white)}

/* nav */
.navbar{left:0;top:44px;width:1200px;height:72px;background:var(--white)}
.brand{left:77px;top:56px;display:flex;align-items:center;gap:10px}
.brand-mark{width:26px;height:26px;background:var(--blue)}
.brand-name{font-size:21px;font-weight:700;color:var(--blue)}
.nav-link{top:72px;font-size:14px;font-weight:600;color:var(--ink)}
.nav-link.active{color:var(--blue)}
.search{left:1112px;top:71px}

/* hero */
.hero{left:0;top:116px;width:1200px;height:511px;background:linear-gradient(100deg,#8a7468 0%,#c9b3a2 30%,#e6dbd0 55%,#cfd3d4 80%,#9aa0a3 100%)}
.hero-panel{left:72px;top:356px;width:1054px;height:225px;background:rgba(20,20,20,.82);clip-path:polygon(3.4% 0,100% 0,98.2% 100%,0 100%)}
.hero-title{left:100px;top:388px;width:1000px;text-align:center;color:var(--white);font-size:32px;line-height:45px;font-weight:400}
.btn-hero{left:499px;top:504px;width:202px;height:43px;border-radius:22px;background:var(--blue);color:var(--white);font-size:14px;font-weight:700;display:flex;align-items:center;justify-content:center}

/* feature */
.feature{left:0;top:627px;width:1200px;height:599px;background:#a3a6ab}
.feature-photo{left:74px;top:691px;width:719px;height:471px;background:linear-gradient(120deg,#1c1c1c 0%,#3a3632 45%,#6b5a4b 65%,#2a2a2a 100%)}
.feature-card{left:793px;top:691px;width:333px;height:471px;background:var(--panel)}
.feature-title{left:793px;top:730px;width:333px;text-align:center;font-family:"Oswald",Arial,sans-serif;font-size:28px;color:var(--black);font-weight:400}
.feature-text{left:821px;top:790px;width:282px;font-size:12px;line-height:20px;color:#222}
.feature-text p+p{margin-top:18px}
.btn-outline{left:870px;top:1027px;width:181px;height:45px;border:1.5px solid var(--black);font-family:"Oswald",Arial,sans-serif;font-size:17px;display:flex;align-items:center;justify-content:center;color:var(--black)}
.arrow{top:1104px}

/* gallery */
.gallery{left:0;top:1226px;width:1200px;height:629px;background:var(--light)}
.tile{width:330px;height:231px;border-radius:3px}
.tile-badge{width:40px;height:40px;background:var(--blue);border-radius:6px}

/* pricing */
.pricing{left:0;top:1855px;width:1200px;height:572px;background:radial-gradient(ellipse at 50% 40%,#3a3a3a 0%,#1a1a1a 55%,#0c0c0c 100%)}
.plan{top:1911px;width:246px;height:462px;background:var(--white);border-radius:3px;overflow:hidden}
.plan-head{height:69px;display:flex;align-items:center;justify-content:center;font-size:18px;font-weight:700;color:var(--grey-text);letter-spacing:.5px}
.plan-price{height:51px;background:#e3e3e3;display:flex;align-items:center;justify-content:center;font-family:"Oswald",Arial,sans-serif;font-size:23px;color:#b0b0b0}
.plan.featured .plan-head{background:var(--yellow);color:var(--white)}
.plan.featured .plan-price{background:#4a4a4a;color:var(--white)}
.plan-list{list-style:none;padding-top:18px;text-align:center;font-size:15px;color:#b4b4b4;line-height:36px}
.plan-list b{color:#9a9a9a}
.plan-btn{position:absolute;left:0;bottom:0;width:246px;height:58px;background:var(--blue);color:var(--white);font-family:"Oswald",Arial,sans-serif;font-size:21px;display:flex;align-items:center;justify-content:center;letter-spacing:.5px}

/* footer */
.footer{left:0;top:2427px;width:1200px;height:137px;background:#f3f4f6}
.footer .brand{top:2482px}
.foot-link{top:2485px;font-size:12px;color:#222}
.social{top:2487px;width:14px;height:14px;border-radius:50%}
.addr{left:884px;top:2459px;font-size:13px;line-height:19px;color:#9a9a9a}
.addr strong{color:#222;font-weight:700}
</style>
</head>
<body>

<header>
  <div class="abs topbar">
    <span class="abs phone">1-800-555-0192</span>
    <span class="abs btn-sm btn-signin">Sign In</span>
    <span class="abs btn-sm btn-signup">Sign Up</span>
  </div>
  <nav class="abs navbar"></nav>
  <div class="abs brand"><span class="brand-mark"></span><span class="brand-name">Corestride Fitness</span></div>
  <a class="abs nav-link active" style="left:451px">HOME</a>
  <a class="abs nav-link" style="left:528px">THE GYM</a>
  <a class="abs nav-link" style="left:624px">THE BOOTCAMP</a>
  <a class="abs nav-link" style="left:762px">PHOTO GALLERY</a>
  <a class="abs nav-link" style="left:906px">ABOUT US</a>
  <a class="abs nav-link" style="left:1009px">CONTACT</a>
  <svg class="abs search" width="14" height="14" viewBox="0 0 14 14"><circle cx="5.5" cy="5.5" r="4.2" fill="none" stroke="#333" stroke-width="1.6"/><line x1="8.6" y1="8.6" x2="12.5" y2="12.5" stroke="#333" stroke-width="1.8"/></svg>
</header>

<section>
  <div class="abs hero" role="img" aria-label="Photo of women training on exercise machines in a bright gym"></div>
  <div class="abs hero-panel"></div>
  <h1 class="abs hero-title">We are a unique personal fitness training service that provides wellness and health training with modern fitness equipment</h1>
  <a class="abs btn-hero">GET MEMBERSHIP NOW</a>
</section>

<section>
  <div class="abs feature" role="img" aria-label="Grey hexagon textured background"></div>
  <div class="abs feature-photo" role="img" aria-label="Photo of a woman lifting a dumbbell in a dark gym"></div>
  <div class="abs feature-card"></div>
  <h2 class="abs feature-title">THE GYM</h2>
  <div class="abs feature-text">
    <p>Lorem ipsum dolor sit amet, consectetur adipiscing elit, sed do eiusmod tempor incididunt ut labore et dolore magna aliqua. Ut enim ad minim veniam, quis nostrud exercitation ullamco laboris nisi ut aliquip ex ea commodo consequat.</p>
    <p>Ut enim ad minim veniam, quis nostrud exercitation ullamco laboris nisi ut aliquip ex ea commodo consequat.</p>
  </div>
  <a class="abs btn-outline">VIEW TIMETABLE</a>
  <svg class="abs arrow" style="left:822px" width="28" height="24" viewBox="0 0 28 24"><path d="M26 12H4M12 3L3 12l9 9" fill="none" stroke="#111" stroke-width="2.6"/></svg>
  <svg class="abs arrow" style="left:1070px" width="28" height="24" viewBox="0 0 28 24"><path d="M2 12h22M16 3l9 9-9 9" fill="none" stroke="var(--blue)" stroke-width="2.6"/></svg>
</section>

<section>
  <div class="abs gallery"></div>
  <div class="abs tile" style="left:74px;top:1282px;background:linear-gradient(120deg,#d9c7b8,#f2eeea 60%,#c9cbcc)" role="img" aria-label="Photo of women running on treadmills"></div>
  <div class="abs tile" style="left:434px;top:1282px;background:linear-gradient(120deg,#2a2a2a,#6a6d70 50%,#1e1e1e)" role="img" aria-label="Photo of a row of exercise bikes"></div>
  <div class="abs tile" style="left:793px;top:1282px;background:linear-gradient(180deg,#c9a47a,#9c8a78 50%,#5a5d62)" role="img" aria-label="Photo of a gym interior with wooden walls"></div>
  <div class="abs tile" style="left:74px;top:1559px;background:linear-gradient(120deg,#e0dcd8,#c3cad1 60%,#8ea9c8)" role="img" aria-label="Photo of a woman stretching in a class"></div>
  <div class="abs tile" style="left:434px;top:1559px;background:linear-gradient(120deg,#d7b58c,#e9d2c6 50%,#a9b9c7)" role="img" aria-label="Photo of an aerobics group class"></div>
  <div class="abs tile" style="left:793px;top:1559px;background:linear-gradient(120deg,#3b3b3b,#8b3a34 55%,#c44b42)" role="img" aria-label="Photo of a boxing class"></div>
  <span class="abs tile-badge" style="left:219px;top:1493px"></span>
  <span class="abs tile-badge" style="left:579px;top:1493px"></span>
  <span class="abs tile-badge" style="left:938px;top:1493px"></span>
  <span class="abs tile-badge" style="left:219px;top:1770px"></span>
  <span class="abs tile-badge" style="left:579px;top:1770px"></span>
  <span class="abs tile-badge" style="left:938px;top:1770px"></span>
</section>

<section>
  <div class="abs pricing" role="img" aria-label="Dark photo of an athlete with dumbbells"></div>

  <div class="abs plan" style="left:74px">
    <div class="plan-head">STRANDARD</div>
    <div class="plan-price">$20/Month</div>
    <ul class="plan-list"><li><b>2x</b> option 1</li><li><b>Free</b> option 2</li><li><b>Unlimited</b> option 3</li><li><b>Unlimited</b> option 4</li><li><b>1x</b> option 5</li><li><b>Free 1</b> class</li><li><b>Free</b> towel</li></ul>
    <a class="plan-btn">REGISTER NOW</a>
  </div>
  <div class="abs plan" style="left:342px">
    <div class="plan-head">BASIC</div>
    <div class="plan-price">$30/Month</div>
    <ul class="plan-list"><li><b>2x</b> option 1</li><li><b>Free</b> option 2</li><li><b>Unlimited</b> option 3</li><li><b>Unlimited</b> option 4</li><li><b>1x</b> option 5</li><li><b>Free 1</b> class</li><li><b>Free</b> towel</li></ul>
    <a class="plan-btn">REGISTER NOW</a>
  </div>
  <div class="abs plan featured" style="left:610px">
    <div class="plan-head">PROFESSIONAL</div>
    <div class="plan-price">$50/Month</div>
    <ul class="plan-list"><li><b>2x</b> option 1</li><li><b>Free</b> option 2</li><li><b>Unlimited</b> option 3</li><li><b>Unlimited</b> option 4</li><li><b>1x</b> option 5</li><li><b>Free 1</b> class</li><li><b>Free</b> towel</li></ul>
    <a class="plan-btn">REGISTER NOW</a>
  </div>
  <div class="abs plan" style="left:879px">
    <div class="plan-head">ULTRA</div>
    <div class="plan-price">$99/Month</div>
    <ul class="plan-list"><li><b>2x</b> option 1</li><li><b>Free</b> option 2</li><li><b>Unlimited</b> option 3</li><li><b>Unlimited</b> option 4</li><li><b>1x</b> option 5</li><li><b>Free 1</b> class</li><li><b>Free</b> towel</li></ul>
    <a class="plan-btn">REGISTER NOW</a>
  </div>
</section>

<footer>
  <div class="abs footer"></div>
  <div class="abs brand"><span class="brand-mark"></span><span class="brand-name">Corestride Fitness</span></div>
  <a class="abs foot-link" style="left:267px">ABOUT US</a>
  <a class="abs foot-link" style="left:359px">MEMBERSHIP</a>
  <a class="abs foot-link" style="left:470px">PHOTOS</a>
  <a class="abs foot-link" style="left:550px">RETAIL SALE</a>
  <a class="abs foot-link" style="left:655px">CONTACT</a>
  <span class="abs social" style="left:742px;background:var(--yellow)"></span>
  <span class="abs social" style="left:782px;background:var(--yellow)"></span>
  <span class="abs social" style="left:822px;background:var(--yellow)"></span>
  <address class="abs addr" style="font-style:normal"><strong>Maple Grove, CA</strong><br>418 Harbor Ln. Suite 22<br>(415) 555-0147</address>
</footer>

</body>
</html>
```